Photography Company Seeks Amazing and Fun Website Design

Note: This is for design only. No coding required. We want to see your ideas for a great website! This will be a FUN design and not boring like others you may work on.

Please let your creative ideas flow. We have given you a ton of info along with videos to help you understand what we are after, however we WANT your creativity to shine through in your designs!

We are a professional company that has run hundreds of crowdsourced projects on multiple platforms. If you participate in this contest (we hope you do) you can expect great video feedback, consistent feedback, and also our guarantee that if we know your website design will not be what we are looking for we will notify you so you don’t waste your time if there is no chance of you winning.

We respect and recognize this is how you make your living and we will not play games. We look forward to an awesome contest and awesome website designs.

Design Brief:

We are looking for a stunning website design to showcase this amazing photography company. Their current site is:

http://www.tervaloshots.example/

As you can see they do amazing photography and need an amazing website to showcase their work and to attract new people into their studios.

We are looking to get a website that is clean, classy, bright, artistic, and that really helps this company stand out amongst other photography companies.

We need a homepage and an interior page mockup.

Here are some examples of other sites in their business with what we like:

http://www.brakovenstudio.example/

Please watch video to learn what we like and don’t like:http://clipvault.example/t/QZpLm4wXr2d

http://www.harbinglenswork.example/

Please watch video to learn what we like and don’t like: http://clipvault.example/t/Wb7gkR2nvsQj

NOTE: We do not want to copy anything outright. We want to learn, model and take their ideas and make them better. We also want to be flexible and take what we like along with your creativity to make an amazing design.

Here is what we are looking for in more specific terms:

NOTE: Website should have a spot for video on the homepage.

This website is for a very professional and well know photography company. Because it is photography the website needs to be VERY visual.

Site should be unique and really stand out to help sell the business and their services. EVERYTHING about this business is visual, so the site MUST reflect that.

Site Overall: Fun and Artistic. This is a forward thinking company that is fun, upbeat, and does things differently, they need the design to reflect that. This is a modern photography company.

They also do all kinds of photography from school kids, sports teams, in studio shoots with High School Seniors, Family Pictures etc.

Colors: We like the white background because it is clean and really helps the photos stand out. Also please look at the logo too. Use colors from that and make things flow. Again we want this to stand out and be different while at the same time being clean.

Menu: Horizontal. We like bold and easy to read menu items. Don’t make it small and cluttered. Include the same items that are in the other site for the mock up.

Site Structure: Clean and easy to navigate. We have a lot of content to display so we need a clean structure that breaks up the text and content areas.

Images: Please pull images from the current site. We can always replace the images of course, but if you show them “their own stuff” in the new design you will be closer to winning because it will feel more like “them”

Content Areas: It is a safe bet that if it is on the current site we need it on the new site. So don’t drop anything as it makes it hard to “cut content”.

What we don't want: We do not want clutter, boring, or templates or themes. We don’t want too cartoony, too cute, or too fancy. We don’t want ugly.

Out of respect to professional designers who really are working hard to win if you do not follow this brief, you submit worn out themes, templates, or boring designs you will be eliminated. We are offering great prize money for this so we expect great visual designs.

Thanks,

The Quillstone Team

Target Market(s)

Target Market are upper middle class who want a better photography studio then the average studio, but don't want to go to the highest end of photography. This studio will cater to higher middle class.

Industry/Entity Type

Business

Number of Pages Required

1 page

Font styles to use
Sans Serif

Requirements
Must have
• Video on Home page
• Clean
• Stand Out
• Fun
• Professional
Nice to have
• Creative
• Lots of content in a great structure
Should not have
• clutter
• ugly design
• messy

```html
<!DOCTYPE html>
<html lang="en">
<head>
<meta charset="utf-8">
<title>Tervalo Photography</title>
<link href="https://fonts.googleapis.com/css2?family=Kreon:wght@300;400;500&display=swap" rel="stylesheet">
<style>
:root{
  --ink:#333333;
  --text:#3a3a3a;
  --rule:#dddddd;
  --accent:#ee5363;
  --footer:#181818;
  --footer-text:#f2f2f2;
  --white:#ffffff;
}
*{box-sizing:border-box;margin:0;padding:0}
html,body{width:1018px;height:1200px;overflow:hidden;background:var(--white)}
body{position:relative;font-family:"Kreon",serif;color:var(--text)}
.site-header{position:absolute;left:0;top:0;width:1018px;height:88px;border-bottom:1px solid var(--rule)}
.nav{position:absolute;top:35px;display:flex;gap:22px;font-size:13px;letter-spacing:-.2px;text-transform:uppercase;color:var(--ink)}
.nav span::after{content:"";display:inline-block;width:4px;height:4px;border-right:1px solid var(--ink);border-bottom:1px solid var(--ink);transform:rotate(45deg);margin:0 0 3px 4px}
.nav-left{left:94px}
.nav-right{right:94px;gap:12px}
.brand{position:absolute;left:455px;top:20px;display:flex;align-items:center;gap:6px;font-size:34px;font-weight:300;color:var(--ink)}
.brand-dot{width:12px;height:12px;border-radius:50%;background:var(--accent)}
.card{position:absolute;width:259px;text-align:center}
.card-photo{height:198px}
.card-title{font-size:21px;color:var(--ink);margin-top:11px;line-height:26px}
.card-text{font-size:13px;line-height:15px;margin-top:4px;letter-spacing:-.2px}
.card-link{position:relative;height:26px;margin-top:10px}
.card-link::before{content:"";position:absolute;left:80px;right:80px;top:13px;border-top:1px solid var(--rule)}
.card-link::after{content:"";position:absolute;left:116px;top:0;width:26px;height:26px;border-radius:50%;background:var(--accent)}
.section-title{position:absolute;left:0;width:1018px;top:840px;text-align:center;font-size:40px;font-weight:400;color:var(--ink)}
.video{position:absolute;top:925px;width:182px;height:142px}
.play{position:absolute;left:74px;top:54px;width:36px;height:36px;border-radius:50%;background:rgba(20,20,20,.85)}
.play::after{content:"";position:absolute;left:14px;top:11px;border-left:11px solid var(--white);border-top:7px solid transparent;border-bottom:7px solid transparent}
.site-footer{position:absolute;left:0;top:1108px;width:1018px;height:92px;background:var(--footer);color:var(--footer-text)}
.footer-nav{position:absolute;left:94px;top:23px;display:flex;gap:20px;font-size:14px}
.copyright{position:absolute;left:94px;top:50px;font-size:14px}
.social{position:absolute;right:94px;top:32px;display:flex;gap:4px}
.social span{width:24px;height:24px;border-radius:50%;background:var(--white)}
</style>
</head>
<body>
<header class="site-header">
  <nav class="nav nav-left"><span>Home</span><span>Studio</span><span>Super Senior Days</span></nav>
  <div class="brand"><span class="brand-dot"></span>Tervalo</div>
  <nav class="nav nav-right"><span>Book It!</span><span>Oerdering</span><span>Sport</span><span>Contact</span></nav>
</header>

<main>
  <article class="card" style="left:94px;top:119px">
    <div class="card-photo" role="img" aria-label="Portrait of a young woman before a colourful mosaic wall" style="background:linear-gradient(135deg,#e9a13a,#3d6fa3,#d8862b)"></div>
    <h2 class="card-title">Girl</h2>
    <p class="card-text">Lorem ipsum dolor sit amet, consectetur elit, sed do eiusmod tempor incididunt ut labore et dolore magna aliqua.</p>
    <div class="card-link"></div>
  </article>
  <article class="card" style="left:380px;top:119px">
    <div class="card-photo" role="img" aria-label="Young boy sitting outdoors with his dog" style="background:linear-gradient(160deg,#2f4f2a,#7aa23c,#b8a487)"></div>
    <h2 class="card-title">Kids</h2>
    <p class="card-text">Lorem ipsum dolor sit amet, consectetur elit, sed do eiusmod tempor incididunt ut labore et dolore magna aliqua.</p>
    <div class="card-link"></div>
  </article>
  <article class="card" style="left:666px;top:119px">
    <div class="card-photo" role="img" aria-label="Close portrait of a smiling young woman against a teal wall" style="background:linear-gradient(135deg,#4fa59a,#b47d62,#3a7f78)"></div>
    <h2 class="card-title">Girl</h2>
    <p class="card-text">Lorem ipsum dolor sit amet, consectetur elit, sed do eiusmod tempor incididunt ut labore et dolore magna aliqua.</p>
    <div class="card-link"></div>
  </article>

  <article class="card" style="left:94px;top:480px">
    <div class="card-photo" role="img" aria-label="Extended family group standing on a lawn" style="background:linear-gradient(180deg,#6c8a5a,#2a2f40,#6b8f3e)"></div>
    <h2 class="card-title">Family</h2>
    <p class="card-text">Lorem ipsum dolor sit amet, consectetur elit, sed do eiusmod tempor incididunt ut labore et dolore magna aliqua.</p>
    <div class="card-link"></div>
  </article>
  <article class="card" style="left:380px;top:480px">
    <div class="card-photo" role="img" aria-label="Businesswoman on the phone in front of a glass building" style="background:linear-gradient(135deg,#7fb0db,#4a86c2,#2b2b2b)"></div>
    <h2 class="card-title">Girl</h2>
    <p class="card-text">Lorem ipsum dolor sit amet, consectetur elit, sed do eiusmod tempor incididunt ut labore et dolore magna aliqua.</p>
    <div class="card-link"></div>
  </article>
  <article class="card" style="left:666px;top:480px">
    <div class="card-photo" role="img" aria-label="Wedding couple walking down stone palace stairs" style="background:linear-gradient(160deg,#d8c8ad,#8a6e55,#b6a98f)"></div>
    <h2 class="card-title">Couples</h2>
    <p class="card-text">Lorem ipsum dolor sit amet, consectetur elit, sed do eiusmod tempor incididunt ut labore et dolore magna aliqua.</p>
    <div class="card-link"></div>
  </article>

  <h2 class="section-title">Some Videos</h2>
  <div class="video" style="left:94px" role="img" aria-label="Video still of a senior in a varsity jacket before a yellow wall"><div style="position:absolute;inset:0;background:linear-gradient(135deg,#c9a531,#2a2a2a)"></div><span class="play"></span></div>
  <div class="video" style="left:310px" role="img" aria-label="Video still of a young woman talking on the phone"><div style="position:absolute;inset:0;background:linear-gradient(135deg,#c8c2bb,#6b2f3d,#a9a39b)"></div><span class="play"></span></div>
  <div class="video" style="left:526px" role="img" aria-label="Video still of a bride on a wooden porch"><div style="position:absolute;inset:0;background:linear-gradient(160deg,#5a3b26,#c2ab8c,#e6e2dc)"></div><span class="play"></span></div>
  <div class="video" style="left:742px" role="img" aria-label="Video still of a wedding couple in a forest"><div style="position:absolute;inset:0;background:linear-gradient(135deg,#7c9a55,#3c4a2c,#d9d9d2)"></div><span class="play"></span></div>
</main>

<footer class="site-footer">
  <nav class="footer-nav"><span>Home</span><span>Studio</span><span>Super Senior Days</span><span>Book It!</span><span>Ordering</span><span>Sports</span><span>Contact Us</span></nav>
  <p class="copyright">Copy right @ 2015 Tervalo Photography. All right reserved</p>
  <div class="social"><span></span><span></span><span></span><span></span></div>
</footer>
</body>
</html>
```